Corveth Thermal Job Add

We need a flashy ad we can post around our marketplace to attract new talent and employee. Our website has our company theme https://corveththermal.ca/

Target Market(s)

HVAC, Refrigeration, Trades

Industry/Entity Type

Trades

Requirements
Must have
• a few key phrases such as "Paying above industry standard" and "No on-call requirements"

```html
<!DOCTYPE html>
<html lang="en">
<head>
<meta charset="utf-8">
<title>Corveth Thermal – We Are Hiring Ad Set</title>
<link rel="stylesheet" href="https://fonts.googleapis.com/css2?family=Montserrat:wght@700;800&display=swap">
<style>
  :root{
    --canvas:#4d4d4f;
    --brand-blue:#1b6fb8;
    --brand-orange:#f15a24;
    --white:#ffffff;
    --photo-dark:#2a2a2d;
    --photo-light:#6e6e72;
  }
  html,body{margin:0;padding:0;overflow:hidden;}
  body{width:923px;height:1200px;background:var(--canvas);position:relative;font-family:"Montserrat",sans-serif;}
  .ad{position:absolute;display:block;}
  .ad text{font-family:"Montserrat",sans-serif;font-weight:700;}
  .fill-blue{fill:var(--brand-blue);}
  .fill-orange{fill:var(--brand-orange);}
  .fill-white{fill:var(--white);}
  .headline{font-weight:800 !important;fill:var(--white);}
  .subhead{fill:var(--white);}
  .perk{fill:var(--white);}
  .url{fill:var(--white);letter-spacing:.5px;}
  .wordmark{fill:var(--brand-blue);font-weight:800 !important;}
  .tick{color:var(--white);}
  .banner-wide{left:32px;top:149px;width:858px;height:166px;}
  .poster-tall{left:32px;top:364px;width:277px;height:554px;}
  .square-a{left:386px;top:364px;width:277px;height:277px;}
  .square-b{left:386px;top:687px;width:277px;height:231px;}
  .skyscraper{left:743px;top:364px;width:147px;height:554px;}
  .banner-slim{left:125px;top:967px;width:672px;height:83px;}
</style>
</head>
<body>

<svg width="0" height="0" style="position:absolute" aria-hidden="true">
  <defs>
    <symbol id="tick-icon" viewBox="0 0 24 24">
      <path d="M20 11.2A8.5 8.5 0 1 1 15.5 4.3" fill="none" stroke="currentColor" stroke-width="2.4" stroke-linecap="round"/>
      <path d="M7.5 11.5l3.5 3.5 9-9" fill="none" stroke="currentColor" stroke-width="2.4" stroke-linecap="round" stroke-linejoin="round"/>
    </symbol>
    <linearGradient id="photo-tone" x1="0" y1="0" x2="1" y2="1">
      <stop offset="0" stop-color="#6e6e72"/>
      <stop offset="0.5" stop-color="#3a3a3d"/>
      <stop offset="1" stop-color="#2a2a2d"/>
    </linearGradient>
  </defs>
</svg>

<!-- Wide leaderboard banner -->
<svg class="ad banner-wide" viewBox="0 0 1561 302">
  <rect class="fill-blue" width="1561" height="302"/>
  <polygon class="fill-white" points="17,0 315,0 340,240 268,302 17,302"/>
  <rect class="fill-orange" width="17" height="302"/>
  <polygon fill="url(#photo-tone)" points="1010,0 1561,0 1561,268 1130,268 1085,55" role="img" aria-label="Photo of a technician in an orange hard hat and safety glasses working on refrigeration equipment"/>
  <rect class="fill-orange" x="1130" y="268" width="431" height="34"/>
  <circle class="fill-orange" cx="180" cy="110" r="38"/>
  <text class="wordmark" x="180" y="190" font-size="30" text-anchor="middle">CORVETH THERMAL</text>
  <text class="headline" x="376" y="100" font-size="76">WE ARE HIRING</text>
  <text class="subhead" x="632" y="172" font-size="46" text-anchor="end">JOIN OUR</text>
  <text class="subhead" x="632" y="228" font-size="46" text-anchor="end">TEAM</text>
  <use href="#tick-icon" class="tick" x="677" y="136" width="28" height="28"/>
  <text class="perk" x="724" y="158" font-size="28">PAYING ABOVE</text>
  <text class="perk" x="724" y="192" font-size="28">INDUSTRY STANDARD</text>
  <use href="#tick-icon" class="tick" x="677" y="222" width="28" height="28"/>
  <text class="perk" x="724" y="243" font-size="28">NO ON-CALL</text>
  <text class="perk" x="724" y="276" font-size="28">REQUIREMENTS</text>
  <text class="url" x="1345" y="293" font-size="20" text-anchor="middle">WWW.CORVETHTHERMAL.CA</text>
</svg>

<!-- Tall portrait poster -->
<svg class="ad poster-tall" viewBox="0 0 504 1008">
  <rect fill="url(#photo-tone)" y="620" width="504" height="353" role="img" aria-label="Photo of a technician in an orange hard hat working on pipework"/>
  <polygon class="fill-blue" points="0,190 504,170 504,728 100,695 0,640"/>
  <polygon class="fill-white" points="0,10 504,10 504,160 400,205 0,195"/>
  <rect class="fill-orange" width="504" height="10"/>
  <rect class="fill-orange" y="973" width="504" height="35"/>
  <circle class="fill-orange" cx="248" cy="72" r="38"/>
  <text class="wordmark" x="248" y="148" font-size="32" text-anchor="middle">CORVETH</text>
  <text class="wordmark" x="248" y="182" font-size="32" text-anchor="middle">THERMAL</text>
  <text class="headline" x="33" y="325" font-size="88">WE ARE</text>
  <text class="headline" x="33" y="405" font-size="88">HIRING</text>
  <text class="subhead" x="33" y="470" font-size="48">JOIN OUR TEAM</text>
  <use href="#tick-icon" class="tick" x="34" y="505" width="26" height="26"/>
  <text class="perk" x="77" y="520" font-size="27">PAYING ABOVE</text>
  <text class="perk" x="77" y="551" font-size="27">INDUSTRY STANDARD</text>
  <use href="#tick-icon" class="tick" x="34" y="578" width="26" height="26"/>
  <text class="perk" x="77" y="597" font-size="27">NO ON-CALL</text>
  <text class="perk" x="77" y="628" font-size="27">REQUIREMENTS</text>
  <text class="url" x="252" y="1000" font-size="25" text-anchor="middle">WWW.CORVETHTHERMAL.CA</text>
</svg>

<!-- Square ad -->
<svg class="ad square-a" viewBox="0 0 504 504">
  <rect class="fill-blue" width="504" height="504"/>
  <polygon fill="url(#photo-tone)" points="270,0 504,0 504,482 245,482 250,370 330,40" role="img" aria-label="Photo of a technician in an orange hard hat and safety glasses"/>
  <polygon class="fill-white" points="0,318 250,370 245,504 0,504"/>
  <rect class="fill-orange" y="495" width="245" height="9"/>
  <rect class="fill-orange" x="245" y="482" width="259" height="22"/>
  <circle class="fill-orange" cx="120" cy="398" r="26"/>
  <text class="wordmark" x="120" y="452" font-size="25" text-anchor="middle">CORVETH</text>
  <text class="wordmark" x="120" y="478" font-size="25" text-anchor="middle">THERMAL</text>
  <text class="headline" x="20" y="80" font-size="54">WE ARE</text>
  <text class="headline" x="20" y="140" font-size="62">HIRING</text>
  <text class="subhead" x="15" y="175" font-size="33">JOIN OUR TEAM</text>
  <use href="#tick-icon" class="tick" x="18" y="198" width="17" height="17"/>
  <text class="perk" x="46" y="209" font-size="18">PAYING ABOVE</text>
  <text class="perk" x="46" y="230" font-size="18">INDUSTRY STANDARD</text>
  <use href="#tick-icon" class="tick" x="18" y="250" width="17" height="17"/>
  <text class="perk" x="46" y="262" font-size="18">NO ON-CALL</text>
  <text class="perk" x="46" y="283" font-size="18">REQUIREMENTS</text>
  <text class="url" x="375" y="498" font-size="13" text-anchor="middle">WWW.CORVETHTHERMAL.CA</text>
</svg>

<!-- Medium rectangle ad -->
<svg class="ad square-b" viewBox="0 0 504 420">
  <rect class="fill-blue" width="504" height="420"/>
  <polygon fill="url(#photo-tone)" points="270,0 504,0 504,396 235,396 240,334 330,40" role="img" aria-label="Photo of a technician in an orange hard hat and safety glasses"/>
  <polygon class="fill-white" points="0,298 240,334 235,420 0,420"/>
  <rect class="fill-orange" y="412" width="235" height="8"/>
  <rect class="fill-orange" x="235" y="396" width="269" height="24"/>
  <circle class="fill-orange" cx="93" cy="348" r="19"/>
  <text class="wordmark" x="93" y="385" font-size="19" text-anchor="middle">CORVETH</text>
  <text class="wordmark" x="93" y="405" font-size="19" text-anchor="middle">THERMAL</text>
  <text class="headline" x="20" y="68" font-size="54">WE ARE</text>
  <text class="headline" x="20" y="128" font-size="62">HIRING</text>
  <text class="subhead" x="17" y="168" font-size="32">JOIN OUR TEAM</text>
  <use href="#tick-icon" class="tick" x="18" y="192" width="17" height="17"/>
  <text class="perk" x="47" y="203" font-size="18">PAYING ABOVE</text>
  <text class="perk" x="47" y="224" font-size="18">INDUSTRY STANDARD</text>
  <use href="#tick-icon" class="tick" x="18" y="243" width="17" height="17"/>
  <text class="perk" x="47" y="255" font-size="18">NO ON-CALL</text>
  <text class="perk" x="47" y="276" font-size="18">REQUIREMENTS</text>
  <text class="url" x="370" y="413" font-size="13" text-anchor="middle">WWW.CORVETHTHERMAL.CA</text>
</svg>

<!-- Skyscraper ad -->
<svg class="ad skyscraper" viewBox="0 0 268 1008">
  <rect fill="url(#photo-tone)" y="660" width="268" height="313" role="img" aria-label="Photo of a technician in an orange hard hat working on pipework"/>
  <polygon class="fill-blue" points="0,225 268,200 268,765 40,720 0,680"/>
  <polygon class="fill-white" points="0,10 268,10 268,200 210,255 0,235"/>
  <rect class="fill-orange" width="268" height="10"/>
  <rect class="fill-orange" y="973" width="268" height="35"/>
  <circle class="fill-orange" cx="134" cy="88" r="36"/>
  <text class="wordmark" x="134" y="162" font-size="30" text-anchor="middle">CORVETH</text>
  <text class="wordmark" x="134" y="194" font-size="30" text-anchor="middle">THERMAL</text>
  <text class="headline" x="134" y="330" font-size="48" text-anchor="middle">WE ARE</text>
  <text class="headline" x="134" y="382" font-size="50" text-anchor="middle">HIRING</text>
  <text class="subhead" x="134" y="434" font-size="25" text-anchor="middle">JOIN OUR TEAM</text>
  <use href="#tick-icon" class="tick" x="14" y="476" width="24" height="24"/>
  <text class="perk" x="55" y="497" font-size="24">PAYING</text>
  <text class="perk" x="55" y="527" font-size="24">ABOVE</text>
  <text class="perk" x="55" y="557" font-size="24">INDUSTRY</text>
  <text class="perk" x="55" y="587" font-size="24">STANDARD</text>
  <use href="#tick-icon" class="tick" x="14" y="626" width="24" height="24"/>
  <text class="perk" x="55" y="647" font-size="24">NO ON-CALL</text>
  <text class="perk" x="55" y="677" font-size="24">REQUIREMENTS</text>
  <text class="url" x="134" y="996" font-size="13" text-anchor="middle">WWW.CORVETHTHERMAL.CA</text>
</svg>

<!-- Slim banner -->
<svg class="ad banner-slim" viewBox="0 0 1223 151">
  <rect class="fill-blue" width="1223" height="151"/>
  <polygon class="fill-white" points="9,0 315,0 325,120 290,151 9,151"/>
  <rect class="fill-orange" width="9" height="151"/>
  <polygon fill="url(#photo-tone)" points="935,0 1223,0 1223,135 995,135 980,40" role="img" aria-label="Photo of a technician in an orange hard hat working on refrigeration equipment"/>
  <rect class="fill-orange" x="995" y="135" width="228" height="16"/>
  <circle class="fill-orange" cx="142" cy="52" r="30"/>
  <text class="wordmark" x="142" y="112" font-size="27" text-anchor="middle">CORVETH</text>
  <text class="wordmark" x="142" y="139" font-size="27" text-anchor="middle">THERMAL</text>
  <text class="headline" x="620" y="45" font-size="40" text-anchor="end">WE ARE</text>
  <text class="headline" x="620" y="98" font-size="52" text-anchor="end">HIRING</text>
  <text class="subhead" x="620" y="135" font-size="30" text-anchor="end">JOIN OUR TEAM</text>
  <use href="#tick-icon" class="tick" x="651" y="18" width="22" height="22"/>
  <text class="perk" x="690" y="36" font-size="23">PAYING ABOVE</text>
  <text class="perk" x="690" y="64" font-size="23">INDUSTRY STANDARD</text>
  <use href="#tick-icon" class="tick" x="651" y="88" width="22" height="22"/>
  <text class="perk" x="690" y="106" font-size="23">NO ON-CALL</text>
  <text class="perk" x="690" y="132" font-size="23">REQUIREMENTS</text>
  <text class="url" x="1109" y="147" font-size="10" text-anchor="middle">WWW.CORVETHTHERMAL.CA</text>
</svg>

</body>
</html>
```